Brochure/flyer for Tuftmoor Nappy Company

My Business name is Plover Wrenlyn Nappies
I am wanting a A4 size brochure (Flyer) to be folded twice. Measurements when folded 210 x 99 mm
I am just about to launch my Modern Cloth Nappy Products and i am wanting a brochure to target new mum's who aren't familiar with Modern cloth nappies and also for mums who are familiar with modern cloth nappies but are looking at trying my brand.
I want the Brochure to be very informative but yet Simple to read. I want people to feel like they want to buy my nappies after they read my Brochure.
The Brochure can be reworded and additional information can be added if you feel its needed, But i would like all the information listed below to be on the brochure.

MOTO: Cloth Nappies The Modern Way

The nappy design is designed in Australia and Australian Owned.

WHY USE CLOTH?
-Save thousands of Dollars
-Easy to use
-Looks Cute
-Super Absorbency
It costs approximately $3000 to use disposable nappies on a child from birth until 2 and a half years, that is Approximately 6000 nappies going into Landfill. This is based on a child going through 6-8 nappies per day.
Modern cloth nappies, on the other hand, cost around $500 for a full stash of 24 nappies. This allows for the child to wear 6-8 nappies per day with a load of nappies going in the wash every 2-3 days. As we have a range of nappies that are one-size-fits-most for bubs ranging from 3kg to 18kg, that $500 would cover your complete stash from birth right through to toilet training, Not to mention the money you would save by using the nappies again for any subsequent Children you may have.
Eliminates your baby's exposure to harmful Chemicals that can be in disposable nappies.
The manufacturing and use of disposable nappies can amount to 2-3 times more wasted water than using cloth nappies
Using Disposable Nappies fill up our landfill, Disposable nappies take more than 100 years to decompose, possibly up to 500 years.

PRODUCTS AVAILABLE:
Newborn: All in One (AIO) Fits approx 2-7kg
Velcro All in Two, One size Fits Most (OSFM) fits approx 3 to 18kg
Snap All in Two, One size Fits Most (OSFM) Fits Approx 3 to 18kg
Extra Inserts
Wetbags
Bamboo Biodegradable liners

The Materials used and features:
All in 2 Nappy (AI2):
Outer Shell Features- A waterproof TPU shell to keep all the wetness in.
Lining is a made of Microfleece material which is soft on baby's skin and Wicks moisture away from the baby's skin it is also very fast drying
Double leg Gussets to avoids any potential side leg Leaks
a poo guard at the back to reduce any leaks from occurring up the back
Insert is Made from 70% Bamboo and 30% Organic Cotton, The extra trim insert with extra absorbency qualities that can easily be double up for a heavy wetting baby or for an all night solution.

Insert snaps in and out Which is easy to remove and replace
A Pocket opening is also available to add a Booster in for long naps or for night time use. Insert is 2 layers sewn together and then folded twice to create 6 layers of absorbency. Unsnap insert from shell for washing, As there is not 3 layers sewn together like most inserts, it dries much quicker and washes more thoroughly, therefore less chance of smells accumulating

Why are these inserts so great?
– Super soft and silky
– Very breathable
– Naturally Anti-bacterial
– Absorbs 3 to 4 times more than cotton
– Doesn't feel sticky or uncomfortable when wet

The newborn nappy has a TPU waterproof Shell and is a all in one (AIO), has 4 layers of absorbency of 70% Bamboo and 30% Organic Cotton, With Microfleece lining which is super soft on newborns delicate skin.
The newborn nappy has a snap to hold down the front of the nappy where the umbilical cord will be for the first week or so. there is also snaps to adjust the size that little bit smaller for Premature babies or small babies. There is also double leg gussets to avoid any leaks around the legs. There is also a Poo guard at the back to avoid any leaks coming up from the back. The waist has a cross over snap for a extra small waist

PRICING:
One Size Fits Most:
Velcro: $25.95
Snap: $25.95
All In One Newborn:
$19.95

PACKAGES:
Price Depends on What nappies you choose for your package

Trial 3 pack: 5% Discount
6 Pack: 10% Discount
12 Pack: 15% Discount
24 Pack: 20% discount

Extra Inserts $7.00
Wetbags: $10
Bamboo Biodegradable Liners: $10
Contact Details:
Jolene Pridmore
Phone: 0491730284
E-mail: ploverwrenlynnappies@mailzenbox.com
Facebook: www.socialnookhub.com/PloverWrenlynNappies

I have changed a few things on the brief so please read carefully before changing or making another design,

Thanks :) 

Target Market(s)

Mums and Dads, care takers, Guardians and grandparents

Industry/Entity Type

Baby

Requirements
Must have
• Must have the Logo and picture i have sent but you are welcome to put other pictures of babies but please do not put pictures of babies with disposable nappies on. and if you are going to put pics of babies i would prefer the pictures not to show how the Velcro or snaps look at the front of the nappy. for example: put pictures that show the nappy side on or from the back. You could put pictures of babies or of nature etc "saving the Environment"
Should not have
• no pictures of other cloth nappy brands No disposable nappies

```html
<!DOCTYPE html>
<html lang="en">
<head>
<meta charset="utf-8">
<title>Plover Wrenlyn Nappies – Inside Spread</title>
<link rel="stylesheet" href="https://fonts.googleapis.com/css2?family=PT+Sans+Narrow:wght@400;700&family=Archivo+Narrow:ital,wght@0,400;0,700;1,400&display=swap">
<style>
  :root {
    --paper: #ffffff;
    --ink: #1c1a1d;
    --plum: #5a1f7c;
    --plum-deep: #3e0f5c;
    --plum-soft: #8a4fae;
  }
  html, body {
    margin: 0;
    padding: 0;
    overflow: hidden;
    background: var(--paper);
  }
  .spread {
    position: relative;
    width: 1200px;
    height: 848px;
    overflow: hidden;
    background: var(--paper);
    color: var(--ink);
    font-family: "Archivo Narrow", "PT Sans Narrow", sans-serif;
    font-size: 12.4px;
    line-height: 15.6px;
  }
  .floral-border {
    position: absolute;
    inset: 0;
    width: 1200px;
    height: 848px;
  }
  .panel {
    position: absolute;
  }
  .panel--why { left: 56px; top: 68px; width: 340px; }
  .panel--materials { left: 423px; top: 68px; width: 356px; }
  .panel--pricing { left: 795px; top: 42px; width: 318px; }
  h2 {
    font-family: "PT Sans Narrow", sans-serif;
    font-weight: 700;
    font-size: 15px;
    line-height: 18px;
    margin: 0 0 2px;
  }
  p { margin: 0; }
  .list {
    list-style: none;
    margin: 0;
    padding: 0;
    font-style: italic;
    font-size: 13.4px;
    line-height: 16.4px;
  }
  .gap { margin-top: 16px; }
  .gap-lg { margin-top: 24px; }
  .products { margin-top: 22px; }
</style>
</head>
<body>
<main class="spread">
  <svg class="floral-border" viewBox="0 0 842 595" preserveAspectRatio="none" role="img" aria-label="Purple side bands with white floral swirl decoration">
    <defs>
      <linearGradient id="plumBand" x1="0" y1="0" x2="1" y2="1">
        <stop offset="0" stop-color="#6a2a8e"/>
        <stop offset="0.6" stop-color="#55197a"/>
        <stop offset="1" stop-color="#3e0f5c"/>
      </linearGradient>
    </defs>
    <path d="M0 0 H30 C22 80 32 160 28 250 C25 330 24 380 32 430 C44 500 72 560 104 595 H0 Z" fill="url(#plumBand)"/>
    <path d="M842 0 H792 C800 80 790 180 794 270 C798 360 776 440 770 500 C766 540 752 570 746 595 H842 Z" fill="url(#plumBand)"/>
  </svg>

  <section class="panel panel--why">
    <h2>WHY USE CLOTH?</h2>
    <ul class="list">
      <li>- Save thousands of Dollars</li>
      <li>- Easy to use</li>
      <li>- Looks Cute</li>
      <li>- Super Absorbency</li>
    </ul>
    <p class="gap">It costs approximately $3000 to use disposable nappies on a child from birth until 2 and a half years, that is Approximately 6000 nappies going into Landfill. This is based on a child going through 6-8 nappies per day.</p>
    <p>Modern cloth nappies, on the other hand, cost around $500 for a full stash of 24 nappies. This allows for the child to wear 6-8 nappies per day with a load of nappies going in the was every 2-3 days. As we have a range of nappies that are one-size-fits-most for bubs ranging from 3kg to 18 kg, that $500 would cover your complete stash from birth right through to toilet training, Not to mention the money you would save by using the nappies again for any subsequent Children you have.</p>
    <p>Eliminates your baby’s exposure to harmful Chemicals that can be in disposable nappies. The manufacturing and use of disposable nappies can amount to 2-3 times more wasted water than using cloth nappies.</p>
    <p>Using Disposable Nappies fill up our landfill, Disposable nappies take more than 100 years to decompose, possible up to 500 years.</p>

    <h2 class="products">PRODUCTS AVAILABLE:</h2>
    <ul class="list">
      <li>Newborn: All in One (AIO) Fits approx Newborn to 6-7kg</li>
      <li>Velcro All in Two, One size Fits Most (OSFM) Fits approx 3 to 18kg</li>
      <li>Snap All in Two, One size Fits Most (OSFM) Fits Approx 3 to 18kg</li>
      <li>Extra Inserts</li>
      <li>Wetbags</li>
      <li>Bamboo Biodegradable liners</li>
    </ul>
  </section>

  <section class="panel panel--materials">
    <h2>The Materials used and features:</h2>
    <p>All in 2 Nappy (AI2)</p>
    <p>Outer Shell Features - A waterproof TPU shell to keep all the wetness in. Linging is a made of Microfleece material which is soft on baby’s skin and Wicks moisture away from the baby’s skin it is also very fast drying.</p>
    <p>Double leg Gussets to avoids any potential side leg Leaks</p>
    <p>a poo guard at the back to reduce any leaks from occurring up the back insert is Made from 70% Bamboo and 30% Organic Cotton, The extra trim insert with extra absorbency qualities that can easily be double up for a heavy wetting baby or for an all night solution.</p>
    <p>Insert snaps in and out Which is easy to remove and replace</p>
    <p>A Pocket opening is also available to add a Booster in for long naps or for ong naps or for night time use. Insert is 2 layers sewn together and then folded twice to create 6 layers of absorbency. Unsnap insert from shell for washing, as there is not 3 layers sewn together like most inserts, it dries much quicker and washes more thoroughly, therefore less chance of smells accumulating.</p>

    <h2 class="gap">Why are these inserts so great?</h2>
    <ul class="list">
      <li>-Super soft and silky</li>
      <li>-Very breathable</li>
      <li>-Naturally Anti-bacterial</li>
      <li>-Absorbs 3 to 4 times more than cotton</li>
      <li>-Doesn’t feel sticky or uncomfortable when wet</li>
    </ul>

    <p class="gap-lg">The newborn nappy has a TPU waterproof Shell and is a all in one (AIO), has 4 layers of absorbency of 70% Bamboo and 30% Organic Cotton, With Microfleece lining which is super soft on newborns delicate skin.</p>
    <p>The newborn nappy has a snap to hold down the front of the nappy where the umbilical cord will be for the first week or so. There is also snaps adjust the size that little bit smaller for Premature babies or small babies. There is also double leg gussets to avoid any leaks around the legs. There is also a Poo guard at the back to avoid any</p>
  </section>

  <section class="panel panel--pricing">
    <p>leaks coming up from the back. The waist has a cross over snap for a extra small waist.</p>

    <h2 class="gap">PRICING:</h2>
    <ul class="list">
      <li>One Size Fits Most:</li>
      <li>Velcro: $25.95</li>
      <li>Snap: $25.95</li>
      <li>All in One Newborn: $19.95</li>
    </ul>

    <h2 class="gap">PACKAGES: Price Depends on What nappies you choose for your package</h2>
    <ul class="list gap">
      <li>Trial 3 pack: 5% Discount</li>
      <li>6 Pack: 10% Discount</li>
      <li>12 Pack: 15% Discount</li>
      <li>24 Pack: 20% Discount</li>
    </ul>
    <ul class="list gap">
      <li>Extra Inserts $7.00</li>
      <li>Wetbags: $10.00</li>
      <li>Bamboo Biodegradable Liners: $10.00</li>
    </ul>
  </section>
</main>
</body>
</html>
```